New logo and wordpress design for Brightmoor-hub.org

We run a website that collates profiles/interviews of individuals who have completed a PhD and moved away from a traditional academix career path into something related. This is often related to the field they studied in, such as publishing, government policy, consulting, teaching and many other things. The website https://brightmoor-hub.org aims to give students and researchers ideas about what paths they can take their career on.

We would like to refresh our brand with a new website and logo. Our website is run through wordpress and hence we would need appropriate files and designs to accomodate this.
Our new logo should represent the idea of navigating a career path and exploring the unknown. Up until now it has been a compass in tones of purple and blue. We are happy to keep this motif but would need an updated, more representative logo. We are also happy to get some new ideas if the designer has something they think would fit.
The website itself should have fresh and clean look. We would like a banner at the top with clear links to the various parts of the site. The banner should stay consistent throughout the site.
We would like the main page to have a clean and simple look which places the focus on the profiles and their associated photos.
We would like pictographs to represent the different fields which our profiles fit into and would like to discuss with the winning designer what these would look like exactly. As a starting point we would like pictographs representing STEM (Science, Technology, Engineering, Mathematics) and SHAPE (Social Sciences, Humanities and Arts for People and the Economy).

We are really looking for something that is clean and professional but embodies our mission to represent all of the major industries which doctoral graduates can go on to work in. Those being, academia (universities), government, industry (private enterprise and companies), and third sector (Charities and think tanks etc.). Any design should cover all of these and not focus just on a big business or similar. It should also represent that we are not purely science focused, but all disciplines and are a broad church in that sense. We are open to various colour schemes and ideas but would like something that gives a professional but approachable feel, it should have elements of Oxford, but not suggest that we are only open to Calderwick University students or graduates.
Some sites that may be useful are:
https://kestrelguild.org/news-resources/projects/research-culture/ - talks about the different areas of employment we are trying to represent
https://www.famden-lv.ac.uk/ an oxford internal website that we like the presentation of.

Target Market(s)

Academic researchers with a PhD

Industry/Entity Type

Academic Careers

Colors
0054AA
0677BA
7BADD7
CADEEF
E8F1F8
00AB8E
00BBA5
67D7C9
C6EFE9
E9F9F6
FFF300
FFF600
FEFA6F
FFFEC7
FFFEE8
6B429C
8869AF
B7A5CE
E3DAEB
F3F0F8

Requirements
Must have
• A new logo
Should not have
• The existing logo

```html
<!DOCTYPE html>
<html lang="en">
<head>
<meta charset="utf-8">
<title>Brightmoor Hub — Explore Your Options Beyond Academia</title>
<link href="https://fonts.googleapis.com/css2?family=Poppins:wght@400;500;600&display=swap" rel="stylesheet">
<style>
  :root{
    --blue:#0054AA;
    --blue-mid:#0677BA;
    --sky:#7BADD7;
    --teal-light:#67D7C9;
    --white:#FFFFFF;
    --ink:#2F2F2F;
    --muted:#7A7A7A;
    --btn:linear-gradient(90deg,#67D7C9,#7BADD7);
  }
  *{box-sizing:border-box;margin:0;padding:0}
  html,body{width:1200px;height:4243px;overflow:hidden}
  body{font-family:'Poppins',sans-serif;background:var(--white);position:relative;color:var(--ink)}
  .abs{position:absolute}
  .btn{position:absolute;background:var(--btn);color:var(--white);border-radius:8px;font-size:17px;display:flex;align-items:center;justify-content:center;text-decoration:none}
  .brand{display:flex;align-items:center;gap:10px;color:var(--white);font-weight:600;font-size:18px}
  .brand-dot{width:22px;height:22px;border-radius:50%;background:var(--white)}

  /* hero */
  .hero{position:absolute;left:0;top:0;width:1200px;height:630px;background:var(--blue)}
  .nav{position:absolute;left:380px;top:38px;display:flex;gap:26px;color:var(--white);font-size:17px}
  .nav .active{text-decoration:underline;font-weight:500}
  .hero-title{left:84px;top:160px;font-size:35px;font-weight:600;line-height:52px;color:var(--white)}
  .hero-text{left:84px;top:272px;width:540px;font-size:19px;line-height:30px;color:var(--white)}
  .avatars{left:84px;top:463px;display:flex}
  .avatar{width:56px;height:56px;border-radius:50%;border:3px solid var(--white);margin-right:-18px;background:linear-gradient(135deg,#c9b8a5,#5d6f86)}
  .hero-caption{left:84px;top:535px;font-size:16px;color:var(--white)}
  .hero-photo{left:665px;top:130px;width:450px;height:440px;border-radius:80px 0 120px 0;background:linear-gradient(135deg,#5b4a3e,#8d7c6b 50%,#4a3a2d)}

  /* generic sections */
  .h2{font-size:30px;font-weight:600;color:var(--ink)}
  .body{font-size:18.5px;line-height:30px;color:var(--muted)}
  .accent{background:var(--blue);border-radius:0 110px 0 110px}
  .photo{box-shadow:14px 18px 30px rgba(0,0,0,.18);border-radius:0 0 80px 0}

  .stats{left:84px;top:1385px;display:flex;gap:26px}
  .stat b{display:block;font-size:29px;font-weight:500;color:var(--ink);padding-left:4px}
  .stat span{display:block;margin-top:12px;font-size:19px;color:var(--muted)}

  .involved{position:absolute;left:0;top:1640px;width:1200px;height:570px;background:var(--blue);color:var(--white)}
  .involved ul{list-style:none}
  .involved li{position:relative;padding-left:30px;font-size:19px;line-height:30px}
  .involved li::before{content:"";position:absolute;left:12px;top:13px;width:5px;height:5px;border-radius:50%;background:var(--white)}

  .card{position:absolute;width:333px;height:381px;overflow:hidden;border-radius:80px 0 80px 0}
  .card.first{border-radius:0 0 80px 0}
  .card .name{position:absolute;left:0;bottom:0;width:260px;height:76px;background:rgba(30,30,30,.55);border-radius:0 30px 0 0;color:var(--white);font-size:19px;font-weight:500;line-height:30px;padding:8px 14px}

  .vacancy{left:84px;top:3425px;width:1031px;height:320px;border-radius:30px 0 60px 0;background:linear-gradient(90deg,#14223a 0%,#28446b 55%,#1b2638 100%);color:var(--white);text-align:center}

  .footer{position:absolute;left:0;top:3845px;width:1200px;height:398px;background:var(--blue);color:var(--white)}
  .footer h4{font-size:21px;font-weight:600;margin-bottom:16px}
  .footer p{font-size:17px;line-height:39px}
  .social{display:flex;gap:24px}
  .social span{width:40px;height:40px;border-radius:50%;background:var(--white)}
</style>
</head>
<body>

<header class="hero">
  <div class="abs brand" style="left:88px;top:34px"><span class="brand-dot"></span>Brightmoor Hub</div>
  <nav class="nav"><span class="active">Home</span><span>About us</span><span>News</span><span>Service</span><span>Testimonials</span></nav>
  <a class="btn" style="left:965px;top:25px;width:150px;height:50px">Contact us</a>

  <h1 class="abs hero-title">Explore Your Options<br>Beyond Academia</h1>
  <p class="abs hero-text">A collection of profiles of people who have made the transition from academia to industry.</p>
  <a class="btn" style="left:84px;top:360px;width:151px;height:51px">Learn More</a>
  <div class="abs avatars" role="img" aria-label="Small round portraits of featured researchers">
    <span class="avatar"></span><span class="avatar"></span><span class="avatar"></span><span class="avatar"></span><span class="avatar"></span>
  </div>
  <p class="abs hero-caption">A collection of profiles of people</p>
  <div class="abs hero-photo" role="img" aria-label="Photo of a smiling woman reading a tablet at a desk"></div>
</header>

<section>
  <div class="abs accent" style="left:84px;top:728px;width:350px;height:225px"></div>
  <div class="abs photo" role="img" aria-label="Photo of two people shaking hands" style="left:142px;top:783px;width:385px;height:292px;border-radius:80px 0 80px 0;background:linear-gradient(120deg,#3d4d63,#b08e74 45%,#cfd6de)"></div>
  <h2 class="abs h2" style="left:596px;top:728px">Career profiles</h2>
  <p class="abs body" style="left:596px;top:783px;width:510px">Explore a collection of profiles from researchers pursuing careers beyond academia. uch diversity in potential roles can prove challenging when exploring your options. This collection of career profiles enables you to see what others in your position chose to do, why and how they made the move, and what they most enjoy about their job.</p>
  <a class="btn" style="left:596px;top:1022px;width:152px;height:52px">Learn More</a>
</section>

<section>
  <h2 class="abs h2" style="left:84px;top:1195px">About Us</h2>
  <p class="abs body" style="left:84px;top:1243px;width:520px">Our role is to source career profiles from a range of fascinating sectors written by researchers with backgrounds spanning the humanities, social sciences, physical and life sciences.</p>
  <div class="abs stats">
    <div class="stat"><b>120+</b><span>verified</span></div>
    <div class="stat"><b>22+</b><span>collaboration</span></div>
    <div class="stat"><b>110K</b><span>product</span></div>
  </div>
  <div class="abs accent" style="left:672px;top:1160px;width:350px;height:225px"></div>
  <div class="abs photo" role="img" aria-label="Photo of a bright open-plan office" style="left:730px;top:1213px;width:385px;height:292px;border-radius:0 0 80px 0;background:linear-gradient(180deg,#d9dde0,#9aa1a6 60%,#3e4246)"></div>
</section>

<section class="involved">
  <div class="abs" role="img" aria-label="Photo of people writing notes at a wooden meeting table" style="left:84px;top:60px;width:426px;height:437px;border-radius:60px 0 80px 0;background:linear-gradient(135deg,#6f6a64,#3a2d25 55%,#1e1814)"></div>
  <h2 class="abs" style="left:571px;top:52px;font-size:30px;font-weight:600">Get involved</h2>
  <p class="abs" style="left:571px;top:100px;width:525px;font-size:19px;line-height:30px">Openings are now available on our team of postdocs, RAs and DPhil students to develop and promote brightmoor-hub.org, featuring profiles of PhD-holders who have moved into a range of jobs beyond academic research and of their employers.</p>
  <ul class="abs" style="left:571px;top:266px;width:525px">
    <li>able to expand the collection in sectors of interest to you</li>
    <li>supported by fellow team-members and the Careers Service</li>
    <li>networking effectively in circles relevant to you</li>
    <li>broadening your communication skills and commercial awareness in ways valued by future employers</li>
  </ul>
</section>

<section>
  <h2 class="abs" style="left:84px;top:2295px;font-size:30px;font-weight:500;line-height:45px;color:var(--ink)">Researchers find all sorts<br>of rewarding careers</h2>
  <p class="abs body" style="left:594px;top:2293px;width:520px">ou will get a feel for their daily activities, workplace culture and work-life balance.Top tip: Look out for authors’ insights into which skills developed during or after their PhD proved helpful in getting their job</p>

  <div class="card first" role="img" aria-label="Portrait photo of a researcher" style="left:84px;top:2497px;background:linear-gradient(160deg,#d8d4cf,#7b6a5e 60%,#2f2a27)"><div class="name">Marisol Quintero-<br>Vega</div></div>
  <div class="card" role="img" aria-label="Portrait photo of a researcher" style="left:433px;top:2497px;background:linear-gradient(160deg,#3a3a3a,#c9a23a 30%,#8c8c8c 65%,#3b3b3b)"><div class="name">Marisol Quintero-<br>Vega</div></div>
  <div class="card" role="img" aria-label="Portrait photo of a researcher by a lake" style="left:783px;top:2497px;background:linear-gradient(160deg,#5f7f48,#3d6a8c 50%,#d9d9d4)"><div class="name">Marisol Quintero-<br>Vega</div></div>
  <div class="card first" role="img" aria-label="Portrait photo of a researcher" style="left:84px;top:2928px;background:linear-gradient(160deg,#f1e4d4,#b88a72 55%,#c59ab0)"><div class="name">Marisol Quintero-<br>Vega</div></div>
  <div class="card" role="img" aria-label="Portrait photo of a researcher" style="left:433px;top:2928px;background:linear-gradient(160deg,#cfd3d8,#8a6b55 50%,#1f1f22)"><div class="name">Marisol Quintero-<br>Vega</div></div>
  <div class="card" role="img" aria-label="Portrait photo of a researcher among flowers" style="left:783px;top:2928px;background:linear-gradient(160deg,#7a6a93,#3a3140 50%,#243a6a)"><div class="name">Marisol Quintero-<br>Vega</div></div>
</section>

<section class="abs vacancy" role="img" aria-label="Background photo of a laptop showing a video call">
  <h2 style="margin-top:42px;font-size:24px;font-weight:600">We are currently opening job vacancies</h2>
  <p style="width:530px;margin:18px auto 0;font-size:19px;line-height:30px">We are looking for new employees for our moving factory. If you are interested in working in the factory, please apply for your job here</p>
  <a class="btn" style="left:436px;top:220px;width:158px;height:50px">Apply Job</a>
</section>

<footer class="footer">
  <div class="abs brand" style="left:90px;top:110px;font-size:17px"><span class="brand-dot"></span>Brightmoor Hub</div>
  <div class="abs social" style="left:84px;top:185px" aria-label="Social links"><span></span><span></span><span></span></div>
  <div class="abs" style="left:409px;top:65px"><h4>Pathers With Us</h4><p>See Our Partners</p><p>Explore Custom Kits</p><p>Receive Volume Discounts</p></div>
  <div class="abs" style="left:688px;top:65px"><h4>Support</h4><p>Customer Support</p><p>Technical Assistance</p><p>Press &amp; Media</p></div>
  <div class="abs" style="left:918px;top:65px"><h4>Contact</h4><p>Exam Request</p><p>Locations</p><p>FAQ</p></div>
  <div class="abs" style="left:84px;top:325px;width:1031px;height:1px;background:rgba(255,255,255,.6)"></div>
  <p class="abs" style="left:0;top:345px;width:1200px;text-align:center;font-size:19px;font-weight:500">All Right Reserved / Privacy Policy / Terms and Conditions</p>
</footer>

</body>
</html>
```